Stationery Design Project

Require letterhead/stationery design based on new logo (see attached).

Would prefer it kept simple but strong and effective.

Target Market(s)

Clients and building developers. Residential/consumer and corporate clientele.

```html
<!DOCTYPE html>
<html lang="en">
<head>
<meta charset="utf-8">
<title>Stonebridge Works Letterhead</title>
<link rel="stylesheet" href="https://fonts.googleapis.com/css2?family=Arimo:wght@400;700&display=swap">
<style>
  :root {
    --backdrop: #e9e6e1;
    --paper: #ffffff;
    --brand-blue: #3dbbeb;
    --ink: #111111;
    --brand-grey: #5f6164;
  }
  html, body {
    margin: 0;
    padding: 0;
    width: 1200px;
    height: 900px;
    overflow: hidden;
    background: var(--backdrop);
    font-family: "Arimo", Arial, sans-serif;
  }
  .canvas {
    position: relative;
    width: 1200px;
    height: 900px;
  }
  .letterhead {
    position: absolute;
    left: 302px;
    top: 25px;
    width: 596px;
    height: 850px;
    background: var(--paper);
    box-shadow: 0 6px 24px rgba(0,0,0,0.18);
    overflow: hidden;
  }
  .letterhead__shapes {
    position: absolute;
    inset: 0;
    width: 100%;
    height: 100%;
  }
  .brand {
    position: absolute;
    top: 34px;
    left: 0;
    right: 0;
    display: flex;
    justify-content: center;
    align-items: center;
    gap: 12px;
  }
  .brand__mark {
    width: 36px;
    height: 36px;
    background: var(--brand-blue);
  }
  .brand__name {
    font-size: 28px;
    font-weight: 400;
    letter-spacing: 1px;
    color: var(--brand-grey);
    text-transform: uppercase;
  }
  .contact {
    position: absolute;
    top: 734px;
    width: 100px;
    margin-left: -50px;
    display: flex;
    flex-direction: column;
    align-items: center;
    gap: 6px;
  }
  .contact__icon {
    width: 28px;
    height: 28px;
    fill: var(--brand-blue);
  }
  .contact__label {
    font-size: 15px;
    font-weight: 700;
    color: var(--ink);
  }
  .contact--phone { left: 53px; }
  .contact--fax { left: 184px; }
  .contact--email { left: 342px; }
  .contact--website { left: 520px; }
</style>
</head>
<body>
<main class="canvas">
  <section class="letterhead">
    <svg class="letterhead__shapes" viewBox="0 0 509 725" preserveAspectRatio="none" aria-hidden="true">
      <path d="M0 60 Q255 140 509 63 L509 160 Q255 75 0 163 Z" fill="var(--brand-blue)"/>
      <path d="M40 725 Q260 670 480 725 Z" fill="var(--brand-blue)"/>
    </svg>

    <header class="brand">
      <span class="brand__mark"></span>
      <span class="brand__name">Stonebridge Works</span>
    </header>

    <footer>
      <div class="contact contact--phone">
        <svg class="contact__icon" viewBox="0 0 24 24" aria-hidden="true">
          <path d="M14 2 l4 1 -1 5 -3 0 c-1 3 -1 6 0 9 l3 0 1 5 -4 1 C9 20 9 5 14 2 Z"/>
        </svg>
        <span class="contact__label">PHONE</span>
      </div>
      <div class="contact contact--fax">
        <svg class="contact__icon" viewBox="0 0 24 24" aria-hidden="true">
          <rect x="6" y="2" width="12" height="7"/>
          <rect x="2" y="10" width="20" height="8" rx="1"/>
          <rect x="5" y="19" width="14" height="3"/>
        </svg>
        <span class="contact__label">FAX</span>
      </div>
      <div class="contact contact--email">
        <svg class="contact__icon" viewBox="0 0 24 24" aria-hidden="true">
          <path d="M2 5 h20 v14 h-20 Z M4 7 v0.5 l8 6 8 -6 V7 Z M4 10 v7 h16 v-7 l-8 6 Z" fill-rule="evenodd"/>
        </svg>
        <span class="contact__label">EMAIL</span>
      </div>
      <div class="contact contact--website">
        <svg class="contact__icon" viewBox="0 0 24 24" aria-hidden="true">
          <circle cx="12" cy="12" r="10"/>
          <path d="M7 8 q3 -2 5 0 q-1 3 -4 3 Z M13 14 q4 -1 5 2 q-3 3 -6 1 Z" fill="var(--paper)"/>
        </svg>
        <span class="contact__label">WEBSITE</span>
      </div>
    </footer>
  </section>
</main>
</body>
</html>
```